Website and Mobile Devices design for food related application.

We need a design that is simple yet playful. The design should be food related if possible.
This design will be on the website and the mobile platform markets we intend application to be deployed too.
This application/website is called "Bitelora[.com]. Its a random restaurant picker for the indecisive users.
Updates
Hi all, I picked a design. Again lots of great designs were submitted but I picked one that was more in line with what I wanted.
Target Market(s)
young internet savvy users.
Industry/Entity Type
Restaurant
Look and feel
Each slider illustrates characteristics of the customer's brand and the style your logo design should communicate.

```html
<!DOCTYPE html>
<html lang="en">
<head>
<meta charset="utf-8">
<title>Bitelora</title>
<link rel="stylesheet" href="https://fonts.googleapis.com/css2?family=Aleo:ital,wght@0,300;0,700;1,700&family=Arimo&display=swap">
<style>
  :root {
    --page-bg: #f1f1f1;
    --header-bg: #ffffff;
    --brand: #c4274c;
    --ink: #2b2b2b;
    --ring: #e1e1e1;
    --ring-edge: #d4d4d4;
    --frame: #f7f6f3;
    --slice-beer: #cc3146;
    --slice-noodles: #3d6a8a;
    --slice-burger: #3aa898;
    --slice-sushi: #42a84b;
    --slice-cupcake: #e2c719;
    --slice-pizza: #f0b13a;
    --button-ink: #555555;
  }
  * { box-sizing: border-box; margin: 0; padding: 0; }
  html, body { width: 1200px; height: 927px; overflow: hidden; }
  body { background: var(--page-bg); font-family: "Aleo", serif; color: var(--ink); }
  .site-header {
    height: 96px; background: var(--header-bg);
    display: flex; align-items: center; justify-content: space-between;
    padding: 0 60px 0 63px;
  }
  .brand-name { font-family: "Aleo", serif; font-weight: 700; font-size: 42px; color: var(--brand); letter-spacing: 0.3px; }
  .nav-link { font-family: "Arimo", sans-serif; font-size: 22px; color: var(--ink); text-decoration: underline; }
  .picker { text-align: center; }
  .picker-prompt { font-family: "Aleo", serif; font-weight: 300; font-size: 28px; margin-top: 73px; }
  .wheel { display: block; margin: 32px auto 0; }
  .spin-label { font-family: "Aleo", serif; font-style: italic; font-weight: 700; font-size: 27px; fill: var(--button-ink); }
</style>
</head>
<body>
  <header class="site-header">
    <span class="brand-name">Bitelora</span>
    <a class="nav-link" href="#">Contacts</a>
  </header>
  <main class="picker">
    <h1 class="picker-prompt">Today I’m feeling....</h1>
    <svg class="wheel" width="580" height="580" viewBox="-290 -290 580 580" aria-label="Food choice wheel">
      <circle class="wheel-ring" r="278" fill="var(--ring)" stroke="var(--ring-edge)" stroke-width="2"/>
      <path class="slice slice-burger" d="M0 0 L256 0 A256 256 0 0 0 128 -221.7 Z" fill="var(--slice-burger)"/>
      <path class="slice slice-sushi" d="M0 0 L256 0 A256 256 0 0 1 128 221.7 Z" fill="var(--slice-sushi)"/>
      <path class="slice slice-cupcake" d="M0 0 L128 221.7 A256 256 0 0 1 -128 221.7 Z" fill="var(--slice-cupcake)"/>
      <path class="slice slice-pizza" d="M0 0 L-128 221.7 A256 256 0 0 1 -256 0 Z" fill="var(--slice-pizza)"/>
      <path class="slice slice-beer" d="M0 0 L-256 0 A256 256 0 0 1 -128 -221.7 Z" fill="var(--slice-beer)"/>
      <path class="slice slice-noodles is-selected" d="M0 0 L-133 -230 A266 266 0 0 1 133 -230 Z" fill="var(--slice-noodles)" stroke="var(--frame)" stroke-width="15" stroke-linejoin="round"/>
      <g class="slice-icons" fill="#ffffff" fill-opacity="0.45">
        <circle role="img" aria-label="Noodle bowl with chopsticks icon" cx="0" cy="-160" r="44"/>
        <circle role="img" aria-label="Burger icon" cx="138" cy="-80" r="44"/>
        <circle role="img" aria-label="Sushi roll with chopsticks icon" cx="138" cy="80" r="44"/>
        <circle role="img" aria-label="Cupcake icon" cx="0" cy="160" r="44"/>
        <circle role="img" aria-label="Pizza with slice icon" cx="-138" cy="80" r="44"/>
        <circle role="img" aria-label="Beer mug icon" cx="-138" cy="-80" r="44"/>
      </g>
      <g class="spin-button">
        <circle r="57" fill="#fbfbfa" stroke="#dcdcdc" stroke-width="2"/>
        <circle r="48" fill="none" stroke="#c9c9c9" stroke-width="1.5"/>
        <text class="spin-label" x="0" y="9" text-anchor="middle">Spin!</text>
      </g>
    </svg>
  </main>
</body>
</html>
```